Real Estate Design Website

I would like to have a design for "real estate agent" website. It needs to be in a "Responsive" framework.

The design need to be suitable for different viewer from all around the world. It needs to be modern. It'd be great if there is a design for mobile and tovix/tablet (it's all under responsive framework). It needs to be easy to navigate and look modern

Target Market(s)

End user/Real estate buyers from different part of the world

Industry/Entity Type

Real Estate

Requirements
Must have
• It's for real estate agent website which is used to represent their brand/image but at the same time it also for their client which is real estate buyers
Should not have
• Should not be boring design/out of date

```html
<!DOCTYPE html>
<html lang="en">
<head>
<meta charset="utf-8">
<title>Nestly — Real Estate</title>
<link rel="stylesheet" href="https://fonts.googleapis.com/css2?family=Open+Sans:wght@400;600;700&family=Bitter:wght@400;700&display=swap">
<style>
:root{
  --green:#8dc63f;
  --cyan:#1ab7ea;
  --orange:#ee8a4b;
  --ink:#333;
  --muted:#777;
  --line:#e1e1e1;
  --panel:#f1f1f1;
  --dark:#3d3d3d;
  --darker:#333;
  --gold:#f3b824;
  --white:#fff;
}
*{box-sizing:border-box;margin:0;padding:0}
html,body{width:1200px;height:2321px;overflow:hidden}
body{font-family:"Open Sans",Arial,sans-serif;color:var(--ink);background:var(--white);font-size:14px;position:relative}
.wrap{position:absolute;left:165px;width:985px}

/* header */
.site-header{position:absolute;top:0;left:0;width:1200px;height:100px}
.brand{position:absolute;left:165px;top:12px;display:flex;align-items:center;gap:8px}
.brand-dot{width:30px;height:30px;border-radius:50%;background:var(--green)}
.brand-name{font-size:28px;font-weight:600;color:#444;font-family:"Open Sans",sans-serif}
.main-nav{position:absolute;left:165px;top:64px;display:flex;gap:0}
.main-nav a{display:block;padding:0 13px;font-size:14px;color:#555;text-decoration:none;line-height:26px;border-bottom:4px solid transparent}
.main-nav a.home{border-bottom-color:var(--cyan);padding:0 10px}
.social-top{position:absolute;left:892px;top:30px;display:flex;gap:25px}
.social-top span{width:38px;height:38px;border-radius:50%;display:block}

/* hero */
.hero{position:absolute;top:102px;left:0;width:1200px;height:378px;background:linear-gradient(120deg,#f2a4a9 0%,#e8c5b3 30%,#b9b0a8 55%,#7f8a7e 100%)}
.hero-tab{position:absolute;left:404px;top:347px;width:406px;height:31px;background:var(--green);display:flex;align-items:center;justify-content:center}

/* stats */
.stats{top:480px;height:92px}
.stat{position:absolute;top:22px;display:flex;align-items:flex-start;gap:14px}
.stat-icon{width:32px;height:32px;background:var(--cyan);display:flex;align-items:center;justify-content:center}
.stat-title{font-size:18px;color:#555;line-height:22px}
.stat-sub{font-size:9px;color:#999}
.stat-num{position:absolute;top:28px;font-size:17px;font-weight:700;color:#333;border-left:1px solid var(--line);padding-left:10px;height:40px;top:20px;line-height:40px}

/* listings */
.listings{position:absolute;top:573px;left:0;width:1200px;height:407px;background:linear-gradient(180deg,#8f8f8f,#a8a8a8 50%,#9a9a9a)}
.arrow{position:absolute;top:180px;width:20px;height:40px;background:#333;display:flex;align-items:center;justify-content:center}
.card{position:absolute;top:44px;width:190px;background:var(--white)}
.card-photo{height:112px}
.card-row{display:flex;justify-content:space-between;height:36px;align-items:center;padding:0 14px;font-size:11px;border-bottom:1px solid #e9e9e9}
.card-row:nth-child(odd){background:#f3f3f3}
.card-row .k{color:#888;font-style:italic}
.card-row .v{font-weight:600;color:#333}
.card-btn{margin:8px auto 0;width:144px;height:28px;background:#3a3a3a;color:var(--gold);font-size:11px;font-weight:700;text-align:center;line-height:28px;position:relative;top:0}
.card-foot{background:#9b9b9b;height:42px;padding-top:6px}

/* search */
.search{top:980px;height:325px}
.search-title{position:absolute;top:50px;display:flex;align-items:center;gap:18px;font-family:"Bitter",serif;font-size:22px;color:#333}
.pin-badge{width:40px;height:40px;border-radius:50%;background:var(--green);display:flex;align-items:center;justify-content:center}
.field{position:absolute}
.field label{display:block;font-size:12px;color:#333;margin-bottom:6px}
.select{height:28px;border:1px solid #d5d5d5;font-size:11px;color:#555;padding-left:10px;line-height:26px;position:relative;background:var(--white)}
.select::after{content:"";position:absolute;right:0;top:0;width:22px;height:26px;border-left:1px solid #e2e2e2}
.btn-search{position:absolute;left:900px;top:236px;width:84px;height:30px;background:var(--orange);color:var(--white);font-size:11px;text-align:center;line-height:30px}

/* intro */
.intro{position:absolute;top:1305px;left:0;width:1200px;height:273px;background:var(--panel)}
.intro h2{position:absolute;left:165px;top:72px;font-size:18px;font-weight:700;letter-spacing:.5px;color:#333}
.intro p{position:absolute;top:120px;width:420px;font-family:"Bitter",serif;font-size:12px;line-height:21px;color:#666}
.intro p em{color:var(--cyan);font-style:normal}

/* offers */
.offers{top:1578px;height:342px}
.offer{position:absolute;top:70px;display:flex;align-items:center;gap:12px}
.offer-badge{width:121px;height:121px;border-radius:50%;background:#e3e3e3;display:flex;align-items:center;justify-content:center}
.offer-img{width:80px;height:80px;border-radius:6px}
.offer small{display:block;font-size:9px;font-weight:700;color:#555;letter-spacing:.5px}
.offer strong{display:block;font-family:"Bitter",serif;font-weight:400;font-size:40px;color:#333;line-height:44px}
.offer a{font-size:10px;color:var(--gold);text-decoration:none}

/* footer */
.site-footer{position:absolute;top:1920px;left:0;width:1200px;height:336px;background:var(--dark)}
.fcol{position:absolute;top:76px}
.fcol h3{font-family:"Bitter",serif;font-weight:400;font-size:17px;color:#eee;letter-spacing:.5px;padding-bottom:10px;border-bottom:1px solid #555;width:200px}
.fcol ul{list-style:none;margin-top:12px}
.fcol li{font-family:"Bitter",serif;font-size:14px;color:#aaa;line-height:27px}
.fcol p{font-family:"Bitter",serif;font-size:13px;color:#6a6a6a;line-height:17px;margin-top:14px;width:190px}
.fsocial{display:flex;gap:12px;margin-top:16px}
.fsocial span{width:28px;height:28px;border-radius:50%;display:block}
.fmail{display:flex;align-items:center;gap:8px;margin-top:20px;font-size:12px;color:#ccc}
.bottom-bar{position:absolute;top:2256px;left:0;width:1200px;height:65px;background:var(--white);border-top:1px solid var(--line)}
.bottom-bar .print{position:absolute;left:0;top:0;width:52px;height:64px;border-right:1px solid var(--line);display:flex;align-items:center;justify-content:center}
.bottom-bar .copy{position:absolute;left:172px;top:24px;font-size:12px;color:#555}
</style>
</head>
<body>

<header class="site-header">
  <div class="brand"><span class="brand-dot"></span><span class="brand-name">Nestly</span></div>
  <nav class="main-nav">
    <a class="home" href="#"><svg width="18" height="16" viewBox="0 0 18 16"><path d="M9 1 1 8h2.5v7h4v-5h3v5h4V8H17z" fill="#333"/></svg></a>
    <a href="#">About us</a><a href="#">Developers</a><a href="#">Spaces for rent</a><a href="#">Services</a><a href="#">News</a><a href="#">Contact</a>
  </nav>
  <div class="social-top">
    <span style="background:#2fa9e1"></span><span style="background:#3b5998"></span><span style="background:#00aff0"></span>
  </div>
</header>

<section class="hero" role="img" aria-label="Aerial photograph of a city skyline with rooftops and streets">
  <div class="hero-tab"><svg width="20" height="12" viewBox="0 0 20 12"><path d="M2 10 10 3l8 7" stroke="#333" stroke-width="3" fill="none"/></svg></div>
</section>

<section class="wrap stats">
  <div class="stat" style="left:2px">
    <div class="stat-icon"><svg width="14" height="18" viewBox="0 0 14 18"><path d="M7 1a6 6 0 0 0-6 6c0 4 6 10 6 10s6-6 6-10a6 6 0 0 0-6-6z" fill="#fff"/><circle cx="7" cy="7" r="2" fill="#1ab7ea"/></svg></div>
    <div><div class="stat-title">Development projects</div><div class="stat-sub">NW02, Sub Zon, Fairview</div></div>
  </div>
  <div class="stat-num" style="left:234px">5</div>
  <div class="stat" style="left:311px">
    <div class="stat-icon"><svg width="16" height="16" viewBox="0 0 16 16"><path d="M8 1 1 7h2v8h10V7h2z" fill="#fff"/></svg></div>
    <div><div class="stat-title">Space for rent</div><div class="stat-sub">NW03, Hale Acre, Factory</div></div>
  </div>
  <div class="stat-num" style="left:500px">92</div>
  <div class="stat" style="left:582px">
    <div class="stat-icon"><svg width="16" height="16" viewBox="0 0 16 16"><path d="M8 1 1 15h14z" fill="#fff"/></svg></div>
    <div><div class="stat-title">Service</div><div class="stat-sub">Building Management, Real Estate Activity</div></div>
  </div>
  <div class="stat-num" style="left:840px">6</div>
</section>

<section class="listings" role="img" aria-label="Faint architectural blueprint background behind property listings">
  <div class="arrow" style="left:144px"><svg width="8" height="12" viewBox="0 0 8 12"><path d="M6 1 1 6l5 5" stroke="#fff" stroke-width="2" fill="none"/></svg></div>
  <div class="arrow" style="left:1036px"><svg width="8" height="12" viewBox="0 0 8 12"><path d="M2 1l5 5-5 5" stroke="#fff" stroke-width="2" fill="none"/></svg></div>

  <article class="card" style="left:183px">
    <div class="card-photo" role="img" aria-label="Photo of a villa terrace with pool and sea view" style="background:linear-gradient(160deg,#6a90b8,#2d3d4f 60%,#8a7a66)"></div>
    <div class="card-row"><span class="k">Property Type:</span><span class="v">Villa</span></div>
    <div class="card-row"><span class="k">Asking Price:</span><span class="v">$6,890,000</span></div>
    <div class="card-row"><span class="k">Rooms:</span><span class="v">4 beds, 3 baths</span></div>
    <div class="card-row"><span class="k">City / Town:</span><span class="v">New York</span></div>
    <div class="card-foot"><div class="card-btn">VIEW PROPERTY</div></div>
  </article>
  <article class="card" style="left:397px">
    <div class="card-photo" role="img" aria-label="Photo of a modern living room with red sofa" style="background:linear-gradient(180deg,#d9d6d2,#8f2236 70%,#e8e4e0)"></div>
    <div class="card-row"><span class="k">Property Type:</span><span class="v">Office Space</span></div>
    <div class="card-row"><span class="k">Asking Price:</span><span class="v">$3,500 / mo.</span></div>
    <div class="card-row"><span class="k">Rooms:</span><span class="v">0 beds, 2 baths</span></div>
    <div class="card-row"><span class="k">City / Town:</span><span class="v">Jersey City</span></div>
    <div class="card-foot"><div class="card-btn">VIEW PROPERTY</div></div>
  </article>
  <article class="card" style="left:613px">
    <div class="card-photo" role="img" aria-label="Photo of a house with a large green lawn" style="background:linear-gradient(180deg,#a9c6e0,#c9c1b0 45%,#5b8a32 65%,#6e9d3d)"></div>
    <div class="card-row"><span class="k">Property Type:</span><span class="v">Office Space</span></div>
    <div class="card-row"><span class="k">Asking Price:</span><span class="v">$2,000,000</span></div>
    <div class="card-row"><span class="k">Rooms:</span><span class="v">6 beds, 4 baths</span></div>
    <div class="card-row"><span class="k">City / Town:</span><span class="v">New York</span></div>
    <div class="card-foot"><div class="card-btn">VIEW PROPERTY</div></div>
  </article>
  <article class="card" style="left:826px">
    <div class="card-photo" role="img" aria-label="Photo of a modern villa at dusk with lit windows" style="background:linear-gradient(180deg,#5c6e86,#3a3a3a 60%,#b08a5a)"></div>
    <div class="card-row"><span class="k">Property Type:</span><span class="v">Villa</span></div>
    <div class="card-row"><span class="k">Asking Price:</span><span class="v">$7,900,000</span></div>
    <div class="card-row"><span class="k">Rooms:</span><span class="v">6 beds, 4 baths</span></div>
    <div class="card-row"><span class="k">City / Town:</span><span class="v">Jersey City</span></div>
    <div class="card-foot"><div class="card-btn">VIEW PROPERTY</div></div>
  </article>
</section>

<section class="wrap search">
  <h2 class="search-title"><span class="pin-badge"><svg width="14" height="18" viewBox="0 0 14 18"><path d="M7 1a6 6 0 0 0-6 6c0 4 6 10 6 10s6-6 6-10a6 6 0 0 0-6-6z" fill="#fff"/><circle cx="7" cy="7" r="2" fill="#8dc63f"/></svg></span>Find your Home</h2>
  <div class="field" style="left:0;top:130px;width:318px"><label>Location</label><div class="select">Select</div></div>
  <div class="field" style="left:341px;top:130px;width:318px"><label>Status</label><div class="select">Select</div></div>
  <div class="field" style="left:675px;top:130px;width:310px"><label>Bedrooms</label><div class="select">Select</div></div>
  <div class="field" style="left:0;top:207px;width:202px"><label>Bathrooms</label><div class="select">Select</div></div>
  <div class="field" style="left:223px;top:207px;width:202px"><label>Minimum Price</label><div class="select">Select</div></div>
  <div class="field" style="left:445px;top:207px;width:202px"><label>Maximum Price</label><div class="select">Select</div></div>
  <div class="field" style="left:671px;top:207px;width:202px"><label>Property Type</label><div class="select">Select</div></div>
  <div class="btn-search">Search</div>
</section>

<section class="intro">
  <h2>WHAT ARE YOU LOOKING FOR?</h2>
  <p style="left:165px">Lorem Ipsum is simply dummy text of the printing and typesetting industry.Lorem Ipsum is simply dummy text of the printing and typesetting industry.<em>Lorem Ipsum</em> is simply dummy text of the printing and typesetting industry.Lorem Ipsum is simply dummy text of the printing and typesetting industry.</p>
  <p style="left:599px">Lorem Ipsum is simply dummy text of the printing and typesetting industry.Lorem Ipsum is simply dummy text of the printing and typesetting industry.Lorem Ipsum is simply dummy text of the printing and typesetting industry.Lorem Ipsum is simply dummy text of the printing and typesetting industry.</p>
</section>

<section class="wrap offers">
  <div class="offer" style="left:0">
    <div class="offer-badge"><div class="offer-img" role="img" aria-label="Illustration of a house" style="background:linear-gradient(160deg,#fafafa,#555)"></div></div>
    <div><small>PROPERTIES FOR</small><strong>SALE</strong><a href="#">View all Properties &gt;&gt;</a></div>
  </div>
  <div class="offer" style="left:285px">
    <div class="offer-badge"><div class="offer-img" role="img" aria-label="Illustration of an apartment building" style="background:linear-gradient(160deg,#d9b27a,#8a5a2e)"></div></div>
    <div><small>APARTMENTS FOR</small><strong>RENT</strong><a href="#">View all Properties &gt;&gt;</a></div>
  </div>
  <div class="offer" style="left:571px">
    <div class="offer-badge"><div class="offer-img" role="img" aria-label="Illustration of an office tower" style="background:linear-gradient(160deg,#bfe4f2,#4b7f96)"></div></div>
    <div><small>OFFICE SPACE FOR</small><strong>LEASE</strong><a href="#">View of Office Spaces &gt;&gt;</a></div>
  </div>
</section>

<footer class="site-footer">
  <div class="fcol" style="left:165px">
    <h3>About Real estate</h3>
    <p>Lorem Ipsum is simply dummy text of the printing and typesetting industry.Lorem Ipsum is simply dummy</p>
    <p>Lorem Ipsum is simply dummy text of the printing</p>
  </div>
  <div class="fcol" style="left:425px">
    <h3>Properties Types</h3>
    <ul><li>Apartment</li><li>Condo</li><li>Multi Family</li><li>Other</li><li>Single Family</li><li>Villa</li></ul>
  </div>
  <div class="fcol" style="left:655px">
    <h3 style="width:150px">Meta</h3>
    <ul><li>Log in</li><li>Entries RSS</li><li>Comments RSS</li><li>Blogsphere.org</li></ul>
  </div>
  <div class="fcol" style="left:829px">
    <h3>Contact Us</h3>
    <div class="fsocial"><span style="background:#2fa9e1"></span><span style="background:#3b5998"></span><span style="background:#d9303a"></span><span style="background:#f08a1c"></span></div>
    <div class="fmail"><svg width="14" height="10" viewBox="0 0 14 10"><rect width="14" height="10" fill="#ccc"/><path d="M0 0l7 5 7-5" stroke="#3d3d3d" fill="none"/></svg>hello@nestly-homes.net</div>
  </div>
</footer>

<div class="bottom-bar">
  <div class="print"><svg width="16" height="14" viewBox="0 0 16 14"><rect x="4" y="0" width="8" height="4" fill="#999"/><rect x="0" y="4" width="16" height="6" fill="#999"/><rect x="4" y="8" width="8" height="6" fill="#ccc"/></svg></div>
  <div class="copy">Copyright © 2013 Nestly Ltd. All rights reserved.</div>
</div>

</body>
</html>
```